Tradeora Banner Design for B2B Consulting Firm

Take the already developed logo (attached) and incorporate it into a creative banner design for placement on Tradeora (the social media platform targeting business users). The banner will be used on the firm's company profile page on Tradeora (not yet created).

```html
<!DOCTYPE html>
<html lang="en">
<head>
<meta charset="utf-8">
<title>Tradeora Banner Concepts – Fractional Marketing Services</title>
<link rel="stylesheet" href="https://fonts.googleapis.com/css2?family=Questrial&family=Gelasio:ital,wght@0,400;1,700&display=swap">
<style>
  :root {
    --canvas-grey: #c8c6c7;
    --forest: #476650;
    --paper: #f5f5f5;
    --white: #f7f7f7;
    --photo-light: #8f9c93;
    --photo-dark: #2a362e;
  }
  * { margin: 0; padding: 0; box-sizing: border-box; }
  html, body { width: 1200px; height: 686px; overflow: hidden; background: var(--canvas-grey); }
  .board { position: relative; width: 1200px; height: 686px; background: var(--canvas-grey); }

  .banner { position: absolute; left: 29px; width: 1143px; overflow: hidden; }
  .banner svg.shapes { position: absolute; inset: 0; }

  .sans { font-family: "Questrial", "Century Gothic", sans-serif; color: var(--white); position: absolute; white-space: nowrap; }
  .title-italic { font-style: italic; font-size: 33px; line-height: 1; }
  .audience { font-size: 22.5px; line-height: 26.5px; }
  .chevrons { position: absolute; }

  /* Concept one */
  .banner--solid { top: 33px; height: 194px; background: var(--forest); }
  .banner--solid .title-italic { left: 211px; top: 80px; }
  .banner--solid .audience { left: 766px; top: 53px; }
  .banner--solid .chevrons--top { left: 733px; top: 31px; }
  .banner--solid .chevrons--bottom { left: 1011px; top: 129px; }

  /* Concept two */
  .banner--arrows { top: 245px; height: 200px; background: var(--white); }
  .banner--arrows .title-italic { left: 155px; top: 68px; line-height: 36px; }
  .banner--arrows .audience { left: 504px; top: 59px; }
  .banner--arrows .chevrons--top { left: 316px; top: 24px; }

  /* Concept three */
  .banner--light { top: 459px; height: 194px; background: var(--paper); }
  .banner--light .rule { position: absolute; left: 307px; top: 44px; width: 64px; height: 3px; background: var(--forest); }
  .serif { font-family: "Gelasio", "Palatino Linotype", Georgia, serif; color: var(--forest); position: absolute; white-space: nowrap; }
  .banner--light .serif-title { left: 306px; top: 55px; font-style: italic; font-weight: 700; font-size: 37px; line-height: 1; }
  .banner--light .serif-audience { left: 306px; top: 111px; font-size: 24.5px; line-height: 30.5px; }
</style>
</head>
<body>
<main class="board">

  <!-- Concept one: solid forest banner -->
  <section class="banner banner--solid">
    <svg class="shapes" width="1143" height="194" viewBox="0 0 1143 194">
      <circle cx="76" cy="162" r="60" fill="var(--white)"/>
    </svg>
    <p class="sans title-italic">Fractional Marketing Services</p>
    <svg class="chevrons chevrons--top" width="30" height="24" viewBox="0 0 30 24" fill="none" stroke="var(--white)" stroke-width="2.2">
      <path d="M2 2 L10 12 L2 22 M10 2 L18 12 L10 22 M18 2 L26 12 L18 22"/>
    </svg>
    <p class="sans audience">For Private Equity Firms,<br>Family Offices &amp;<br>Investment Banks</p>
    <svg class="chevrons chevrons--bottom" width="30" height="24" viewBox="0 0 30 24" fill="none" stroke="var(--white)" stroke-width="2.2">
      <path d="M2 2 L10 12 L2 22 M10 2 L18 12 L10 22 M18 2 L26 12 L18 22"/>
    </svg>
  </section>

  <!-- Concept two: arrow panels with photo -->
  <section class="banner banner--arrows">
    <svg class="shapes" width="1143" height="200" viewBox="0 0 1143 200">
      <defs>
        <linearGradient id="photoTone" x1="0" y1="0" x2="1" y2="0">
          <stop offset="0" stop-color="var(--photo-dark)"/>
          <stop offset="0.45" stop-color="var(--photo-light)"/>
          <stop offset="1" stop-color="var(--photo-dark)"/>
        </linearGradient>
        <clipPath id="innerBand"><rect x="0" y="6" width="1143" height="188"/></clipPath>
      </defs>
      <polygon points="0,6 389,6 457,100 389,194 0,194" fill="var(--forest)"/>
      <polygon points="397,6 744,6 812,100 744,194 397,194 465,100" fill="var(--forest)"/>
      <polygon role="img" aria-label="Photo: two business people shaking hands in an office" points="752,6 1143,6 1143,194 752,194 820,100" fill="url(#photoTone)"/>
      <circle cx="76" cy="164" r="60" fill="var(--white)" clip-path="url(#innerBand)"/>
    </svg>
    <svg class="chevrons chevrons--top" width="30" height="24" viewBox="0 0 30 24" fill="none" stroke="var(--white)" stroke-width="2.2">
      <path d="M2 2 L10 12 L2 22 M10 2 L18 12 L10 22 M18 2 L26 12 L18 22"/>
    </svg>
    <p class="sans title-italic">Fractional<br>Marketing Services</p>
    <p class="sans audience">For Private Equity Firms,<br>Family Offices &amp;<br>Investment Banks</p>
  </section>

  <!-- Concept three: light banner with serif type -->
  <section class="banner banner--light">
    <svg class="shapes" width="1143" height="194" viewBox="0 0 1143 194">
      <circle cx="77" cy="162" r="60" fill="var(--forest)"/>
      <polygon points="1017,5 1047,5 1118,96 1047,190 1017,190 1086,96" fill="var(--forest)"/>
      <polygon points="1052,0 1143,0 1143,194 1052,194 1123,96" fill="var(--forest)"/>
    </svg>
    <span class="rule"></span>
    <h2 class="serif serif-title">Fractional Marketing Services</h2>
    <p class="serif serif-audience">For Private Equity Firms, Family Offices &amp;<br>Investment Banks</p>
  </section>

</main>
</body>
</html>
```